web page look and feel - B2B enterprise application

We have an enterprise application with 10 to 15 core pages and several supporting pages or popups. To start, we want the graphical design of the Users, Roles and Data Source pages and their supporting popups, wizards, etc. to be made beautiful. That is around 10 pages in total. There is a fair amount of redundancy among the pages. I have attached 5 screenshots. We very much want the pages to project a premium feel. That is absolutely essential. The color scheme is blue and sometimes yellow (only if it makes the page look better) plus black, gray and white. If the design of these screens goes well, we would expand the project to continue with other pages. The core of what we are looking for is graphic in nature but we are open to workflow suggestions if you have them. The Roles screen needs some improvements to the layout. I am looking for everything that includes icons, fonts, spacing, etc. I assume getting to the final design will take some back and forth with multiple revisions.

Target Market(s)

Large Enterprises

Number of Pages Required

5+ page

Requirements
Must have
• Premium feel

```html
<!DOCTYPE html>
<html lang="en">
<head>
<meta charset="utf-8">
<title>Roles – Norvale Data</title>
<link rel="stylesheet" href="https://fonts.googleapis.com/css2?family=Mulish:wght@400;500;600;700&display=swap">
<style>
  :root{
    --navy:#2b2a63;
    --topbar:#1f1f22;
    --blue:#2f6db3;
    --yellow:#f9c51b;
    --canvas:#fdf3ef;
    --white:#ffffff;
    --ink:#333338;
    --muted:#6b6b72;
    --line:#d9d6d6;
    --row-alt:#f5f4f4;
  }
  *{box-sizing:border-box;margin:0;padding:0}
  html,body{width:1200px;height:818px;overflow:hidden}
  body{font-family:"Mulish",Arial,sans-serif;color:var(--ink);background:var(--canvas);position:relative}
  .sidebar{position:absolute;left:0;top:0;width:261px;height:818px;background:var(--navy)}
  .brand{position:absolute;left:0;top:0;width:261px;height:62px;background:#1a1a1c;display:flex;align-items:center;padding-left:42px;gap:10px}
  .brand-dot{width:12px;height:12px;border-radius:50%;background:var(--yellow)}
  .brand-name{color:var(--white);font-size:19px;font-weight:500;letter-spacing:.2px}
  .nav{position:absolute;top:116px;left:0;list-style:none}
  .nav li{height:39.2px;display:flex;align-items:center;color:var(--white);font-size:12.5px;padding-left:38px}
  .nav .ico{width:32px;display:flex;align-items:center}
  .nav .ico svg{width:14px;height:14px;fill:var(--white)}
  .topbar{position:absolute;left:261px;top:0;right:0;height:62px;background:linear-gradient(180deg,#2a2a2d,#1c1c1e)}
  .topbar svg{position:absolute;fill:var(--white)}
  .user{position:absolute;left:816px;top:22px;color:var(--white);font-size:15px}
  .page-title{position:absolute;left:282px;top:114px;font-size:26px;font-weight:500;color:#2a2a2e}
  .btn-add{position:absolute;left:373px;top:115px;width:57px;height:31px;background:var(--blue);color:var(--white);border-radius:3px;font-size:13.5px;font-weight:600;display:flex;align-items:center;justify-content:center}
  .search{position:absolute;left:826px;top:114px;width:334px;height:40px;background:var(--white);border:1px solid #ece6e3}
  .search-btn{position:absolute;right:-1px;top:-1px;width:43px;height:40px;background:var(--blue);display:flex;align-items:center;justify-content:center}
  .adv{position:absolute;right:39px;top:168px;font-size:12.5px;color:#3a3a40}
  .roles{position:absolute;left:283px;top:212px;border-collapse:collapse;table-layout:fixed;width:877px}
  .roles th{background:var(--navy);color:var(--white);font-weight:500;font-size:11.5px;height:38px;border-right:1px solid #4b4a80;white-space:nowrap;padding:0}
  .roles th.name{text-align:left;padding-left:12px}
  .roles th.blank{border-right:none}
  .roles td{height:45.6px;border:1px solid var(--line);font-size:10.5px;color:var(--muted);text-align:center;padding:0;background:var(--white)}
  .roles tr:nth-child(even) td{background:var(--row-alt)}
  .roles td.name{text-align:left;padding-left:12px;font-size:12px;color:#45454b}
  .stack span,.inline span{display:flex;align-items:center;gap:3px;justify-content:center;line-height:17.5px}
  .stack{display:inline-flex;flex-direction:column;align-items:flex-start}
  .inline{display:flex;justify-content:center;gap:6px}
  .chk{width:9px;height:9px;stroke:var(--blue);fill:none}
  .roles td.act{background:var(--blue)!important;border-color:#5385c1}
  .roles td.act svg{width:11px;height:11px;stroke:var(--white);fill:none;stroke-width:1.6}
  .pager{position:absolute;top:520px;left:0;width:1200px;height:27px}
  .pager svg{position:absolute;top:8px;fill:#3b3b44}
  .pg{position:absolute;top:0;height:27px;border-radius:3px;display:flex;align-items:center;justify-content:center;font-size:13px;font-weight:700}
  .pg.cur{left:666px;width:35px;background:var(--navy);color:var(--white)}
  .pg.size{left:819px;width:35px;background:var(--yellow);color:var(--white)}
  .footer{position:absolute;left:261px;top:744px;width:939px;height:74px;background:var(--white);text-align:center;padding-top:26px;font-size:11.5px;color:#8a8a90}
</style>
</head>
<body>
<svg width="0" height="0" style="position:absolute">
  <symbol id="on" viewBox="0 0 10 10"><rect x="1" y="1" width="8" height="8" rx="1.3" stroke-width="1.2"/><path d="M3 5l1.6 1.6L8.5 2.5" stroke-width="1.4"/></symbol>
  <symbol id="off" viewBox="0 0 10 10"><rect x="1" y="1" width="8" height="8" rx="1.3" stroke-width="1.2"/></symbol>
  <symbol id="copy" viewBox="0 0 12 12"><rect x="4" y="1.5" width="6.5" height="6.5" rx="1"/><path d="M8 8v2.5H1.5V4H4"/></symbol>
  <symbol id="edit" viewBox="0 0 12 12"><path d="M9 7v3.5H1.5V3H5"/><path d="M5 7.3l.3-1.8L9.5 1.3l1.3 1.3-4.2 4.2z"/></symbol>
  <symbol id="trash" viewBox="0 0 12 12"><path d="M2 3h8M4.5 3V1.5h3V3M3 3l.6 7.5h4.8L9 3M5 5v4M7 5v4"/></symbol>
</svg>

<aside class="sidebar">
  <div class="brand"><span class="brand-dot"></span><span class="brand-name">Norvale Data</span></div>
  <ul class="nav">
    <li><span class="ico"><svg viewBox="0 0 16 16"><circle cx="8" cy="5" r="3"/><circle cx="3" cy="6" r="2"/><circle cx="13" cy="6" r="2"/><path d="M3 14c0-3 2-5 5-5s5 2 5 5zM0 13c0-2 1-4 3-4 1 0 1 1 1 1l-1 3zM16 13c0-2-1-4-3-4-1 0-1 1-1 1l1 3z"/></svg></span>Users</li>
    <li><span class="ico"></span>Roles</li>
    <li><span class="ico"></span>Notification Groups</li>
    <li><span class="ico"><svg viewBox="0 0 16 16"><ellipse cx="8" cy="3" rx="6" ry="2.2"/><path d="M2 5c0 1.2 2.7 2.2 6 2.2S14 6.2 14 5v2.5c0 1.2-2.7 2.2-6 2.2S2 8.7 2 7.5zM2 10c0 1.2 2.7 2.2 6 2.2s6-1 6-2.2v2.5c0 1.2-2.7 2.2-6 2.2s-6-1-6-2.2z"/></svg></span>Data Sources</li>
    <li><span class="ico"><svg viewBox="0 0 16 16"><rect x="1" y="2" width="4" height="3"/><rect x="6" y="2" width="4" height="3"/><rect x="11" y="2" width="4" height="3"/><rect x="1" y="6.5" width="4" height="3"/><rect x="6" y="6.5" width="4" height="3"/><rect x="11" y="6.5" width="4" height="3"/><rect x="1" y="11" width="4" height="3"/><rect x="6" y="11" width="4" height="3"/><rect x="11" y="11" width="4" height="3"/></svg></span>Data Object Relationships</li>
    <li><span class="ico"><svg viewBox="0 0 16 16"><rect x="1" y="2" width="6" height="5" rx="1"/><rect x="9" y="2" width="6" height="5" rx="1"/><rect x="1" y="9" width="6" height="5" rx="1"/><rect x="9" y="9" width="6" height="5" rx="1"/></svg></span>Data Sets</li>
    <li><span class="ico"><svg viewBox="0 0 16 16"><rect x="3" y="2" width="12" height="2"/><rect x="1" y="6" width="14" height="2"/><rect x="3" y="10" width="12" height="2"/><rect x="1" y="13" width="14" height="2"/></svg></span>Rule Sets</li>
    <li><span class="ico"><svg viewBox="0 0 16 16"><path d="M8 1a7 7 0 1 0 0 14A7 7 0 0 0 8 1zm0 2.2a4.8 4.8 0 1 1 0 9.6 4.8 4.8 0 0 1 0-9.6zM7.2 4.5h1.6v3.2H11v1.6H7.2z"/></svg></span>Schedule</li>
    <li><span class="ico"><svg viewBox="0 0 16 16"><path d="M3 5h8V3l4 3-4 3V7H5v2H3zM13 11H5v2l-4-3 4-3v2h6V7h2z"/></svg></span>Metadata Import/Export</li>
    <li><span class="ico"></span>Import</li>
    <li><span class="ico"></span>Export</li>
  </ul>
</aside>

<header class="topbar">
  <svg style="left:22px;top:22px" width="20" height="17" viewBox="0 0 20 17"><rect y="0" width="20" height="3"/><rect y="7" width="20" height="3"/><rect y="14" width="20" height="3"/></svg>
  <svg style="left:585px;top:22px" width="22" height="19" viewBox="0 0 22 19"><path d="M11 1A10 10 0 0 0 1 11c0 2.7 1 5.2 2.8 7h14.4A10 10 0 0 0 11 1zm0 3a1.2 1.2 0 1 1 0 2.4A1.2 1.2 0 0 1 11 4zM5 10a1.2 1.2 0 1 1 0 2.4A1.2 1.2 0 0 1 5 10zm12 0a1.2 1.2 0 1 1 0 2.4 1.2 1.2 0 0 1 0-2.4zM7 6a1.2 1.2 0 1 1 0 2.4A1.2 1.2 0 0 1 7 6zm8 0a1.2 1.2 0 1 1 0 2.4A1.2 1.2 0 0 1 15 6zm-4 7.5a2 2 0 0 1-.6-3.9L12 7l.2 3a2 2 0 0 1-1.2 3.5z"/></svg>
  <svg style="left:630px;top:21px" width="20" height="20" viewBox="0 0 20 20"><path d="M2 17L13 6l1.5 1.5L3.5 18.5z"/><path d="M15 1l.6 1.8L17.4 3l-1.8.6L15 5.4l-.6-1.8L12.6 3l1.8-.6zM18.5 7l.4 1.1 1.1.4-1.1.4-.4 1.1-.4-1.1L17 8.5l1.1-.4zM9.5 1.5l.4 1.1 1.1.4-1.1.4-.4 1.1-.4-1.1L8 3l1.1-.4z"/></svg>
  <svg style="left:672px;top:21px" width="20" height="20" viewBox="0 0 20 20"><path d="M10 0a10 10 0 1 0 0 20 10 10 0 0 0 0-20zm0 16.2a1.4 1.4 0 1 1 0-2.8 1.4 1.4 0 0 1 0 2.8zm1.3-5v.8H8.7v-1.3c0-1.8 2.6-2 2.6-3.3 0-.7-.6-1.2-1.4-1.2-.8 0-1.4.5-1.6 1.3L6.1 7c.3-1.8 1.9-3.1 3.9-3.1 2.2 0 3.9 1.3 3.9 3.3 0 2.1-2.6 2.6-2.6 4z"/></svg>
  <svg style="left:714px;top:21px" width="20" height="20" viewBox="0 0 20 20"><path d="M8.5 0h3l.5 2.6 1.8.8 2.2-1.5 2.1 2.1-1.5 2.2.8 1.8 2.6.5v3l-2.6.5-.8 1.8 1.5 2.2-2.1 2.1-2.2-1.5-1.8.8-.5 2.6h-3L8 17.4l-1.8-.8L4 18.1 1.9 16l1.5-2.2-.8-1.8L0 11.5v-3L2.6 8l.8-1.8L1.9 4 4 1.9l2.2 1.5L8 2.6zM10 6.6a3.4 3.4 0 1 0 0 6.8 3.4 3.4 0 0 0 0-6.8z"/></svg>
  <div class="user">Dana Reyes <svg style="position:static;vertical-align:middle;margin-left:6px;fill:none;stroke:#fff;stroke-width:1.8" width="10" height="7" viewBox="0 0 10 7"><path d="M1 1l4 4 4-4"/></svg></div>
</header>

<h1 class="page-title">Roles</h1>
<div class="btn-add">ADD</div>
<div class="search"><div class="search-btn"><svg width="15" height="15" viewBox="0 0 16 16" fill="none" stroke="#fff" stroke-width="2.4"><circle cx="6.5" cy="6.5" r="4.5"/><path d="M10 10l4.5 4.5"/></svg></div></div>
<div class="adv">Advanced Search</div>

<table class="roles">
  <colgroup>
    <col style="width:107px"><col style="width:86px"><col style="width:64px"><col style="width:62px"><col style="width:68px"><col style="width:101px"><col style="width:121px"><col style="width:135px"><col style="width:47px"><col style="width:28px"><col style="width:28px"><col style="width:30px">
  </colgroup>
  <thead>
    <tr>
      <th class="name">Role Name <svg style="margin-left:10px;vertical-align:middle" width="8" height="5" viewBox="0 0 8 5" fill="#fff"><path d="M0 0h8L4 5z"/></svg></th>
      <th>Data Sources</th><th>Data Sets</th><th>Rule Sets</th><th>Schedules</th><th>Suspect Matches</th><th>Master Data Objects</th><th>Metdata Import/Export</th><th>API</th><th colspan="3" class="blank"></th>
    </tr>
  </thead>
  <tbody>
    <tr>
      <td class="name">System Admin</td>
      <td><div class="stack"><span><svg class="chk"><use href="#on"/></svg>Read</span><span><svg class="chk"><use href="#on"/></svg>Write</span></div></td>
      <td><div class="stack"><span><svg class="chk"><use href="#on"/></svg>Read</span><span><svg class="chk"><use href="#off"/></svg>Write</span></div></td>
      <td><div class="stack"><span><svg class="chk"><use href="#on"/></svg>Read</span><span><svg class="chk"><use href="#on"/></svg>Write</span></div></td>
      <td><div class="stack"><span><svg class="chk"><use href="#on"/></svg>Read</span><span><svg class="chk"><use href="#off"/></svg>Write</span></div></td>
      <td><div class="inline"><span><svg class="chk"><use href="#on"/></svg>Read</span><span><svg class="chk"><use href="#on"/></svg>Write</span></div></td>
      <td><div class="inline"><span><svg class="chk"><use href="#on"/></svg>Read</span><span><svg class="chk"><use href="#on"/></svg>Write</span></div></td>
      <td><div class="inline"><span><svg class="chk"><use href="#on"/></svg>Read</span><span><svg class="chk"><use href="#off"/></svg>Write</span></div></td>
      <td><div class="stack"><span><svg class="chk"><use href="#on"/></svg>Read</span><span><svg class="chk"><use href="#off"/></svg>Write</span></div></td>
      <td class="act"><svg><use href="#copy"/></svg></td><td colspan="2"></td>
    </tr>
    <tr>
      <td class="name">Role#1</td>
      <td><div class="stack"><span><svg class="chk"><use href="#on"/></svg>Read</span><span><svg class="chk"><use href="#on"/></svg>Write</span></div></td>
      <td><div class="stack"><span><svg class="chk"><use href="#on"/></svg>Read</span><span><svg class="chk"><use href="#off"/></svg>Write</span></div></td>
      <td><div class="stack"><span><svg class="chk"><use href="#on"/></svg>Read</span><span><svg class="chk"><use href="#on"/></svg>Write</span></div></td>
      <td><div class="stack"><span><svg class="chk"><use href="#on"/></svg>Read</span><span><svg class="chk"><use href="#off"/></svg>Write</span></div></td>
      <td><div class="inline"><span><svg class="chk"><use href="#on"/></svg>Read</span><span><svg class="chk"><use href="#on"/></svg>Write</span></div></td>
      <td><div class="inline"><span><svg class="chk"><use href="#on"/></svg>Read</span><span><svg class="chk"><use href="#on"/></svg>Write</span></div></td>
      <td><div class="inline"><span><svg class="chk"><use href="#on"/></svg>Read</span><span><svg class="chk"><use href="#off"/></svg>Write</span></div></td>
      <td><div class="stack"><span><svg class="chk"><use href="#on"/></svg>Read</span><span><svg class="chk"><use href="#off"/></svg>Write</span></div></td>
      <td class="act"><svg><use href="#copy"/></svg></td><td colspan="2"></td>
    </tr>
    <tr>
      <td class="name">Read Only</td>
      <td><div class="stack"><span><svg class="chk"><use href="#on"/></svg>Read</span><span><svg class="chk"><use href="#on"/></svg>Write</span></div></td>
      <td><div class="stack"><span><svg class="chk"><use href="#on"/></svg>Read</span><span><svg class="chk"><use href="#off"/></svg>Write</span></div></td>
      <td><div class="stack"><span><svg class="chk"><use href="#on"/></svg>Read</span><span><svg class="chk"><use href="#on"/></svg>Write</span></div></td>
      <td><div class="stack"><span><svg class="chk"><use href="#on"/></svg>Read</span><span><svg class="chk"><use href="#off"/></svg>Write</span></div></td>
      <td><div class="inline"><span><svg class="chk"><use href="#on"/></svg>Read</span><span><svg class="chk"><use href="#on"/></svg>Write</span></div></td>
      <td><div class="inline"><span><svg class="chk"><use href="#on"/></svg>Read</span><span><svg class="chk"><use href="#on"/></svg>Write</span></div></td>
      <td><div class="inline"><span><svg class="chk"><use href="#on"/></svg>Read</span><span><svg class="chk"><use href="#off"/></svg>Write</span></div></td>
      <td><div class="stack"><span><svg class="chk"><use href="#on"/></svg>Read</span><span><svg class="chk"><use href="#off"/></svg>Write</span></div></td>
      <td class="act"><svg><use href="#edit"/></svg></td><td class="act"><svg><use href="#copy"/></svg></td><td class="act"><svg><use href="#trash"/></svg></td>
    </tr>
    <tr>
      <td class="name">Data Admin</td>
      <td><div class="stack"><span><svg class="chk"><use href="#on"/></svg>Read</span><span><svg class="chk"><use href="#on"/></svg>Write</span></div></td>
      <td><div class="stack"><span><svg class="chk"><use href="#on"/></svg>Read</span><span><svg class="chk"><use href="#off"/></svg>Write</span></div></td>
      <td><div class="stack"><span><svg class="chk"><use href="#on"/></svg>Read</span><span><svg class="chk"><use href="#on"/></svg>Write</span></div></td>
      <td><div class="stack"><span><svg class="chk"><use href="#on"/></svg>Read</span><span><svg class="chk"><use href="#off"/></svg>Write</span></div></td>
      <td><div class="inline"><span><svg class="chk"><use href="#on"/></svg>Read</span><span><svg class="chk"><use href="#on"/></svg>Write</span></div></td>
      <td><div class="inline"><span><svg class="chk"><use href="#on"/></svg>Read</span><span><svg class="chk"><use href="#on"/></svg>Write</span></div></td>
      <td><div class="inline"><span><svg class="chk"><use href="#on"/></svg>Read</span><span><svg class="chk"><use href="#off"/></svg>Write</span></div></td>
      <td><div class="stack"><span><svg class="chk"><use href="#on"/></svg>Read</span><span><svg class="chk"><use href="#off"/></svg>Write</span></div></td>
      <td class="act"><svg><use href="#copy"/></svg></td><td colspan="2"></td>
    </tr>
  </tbody>
</table>

<nav class="pager">
  <svg style="left:588px" width="10" height="11" viewBox="0 0 10 11"><rect x="1" width="2" height="11"/><path d="M9 0v11L3 5.5z"/></svg>
  <svg style="left:618px" width="13" height="11" viewBox="0 0 13 11"><path d="M6.5 0v11L0 5.5zM13 0v11L6.5 5.5z"/></svg>
  <div class="pg cur">1</div>
  <svg style="left:736px" width="13" height="11" viewBox="0 0 13 11"><path d="M0 0v11l6.5-5.5zM6.5 0v11L13 5.5z"/></svg>
  <svg style="left:769px" width="10" height="11" viewBox="0 0 10 11"><path d="M1 0v11l6-5.5z"/><rect x="7" width="2" height="11"/></svg>
  <div class="pg size">20</div>
</nav>

<footer class="footer">Copyright 2018 Norvale Data.All Rights Reserved | Privacy Statement | Terms Of Use</footer>
</body>
</html>
```